Personnel recruitment Brauwalter GmbH

We would like to create an attractive flyer that focuses on one of our services in Saarland and Rhineland-Palatinate. The benefits for the customer should be presented.

```html
<!DOCTYPE html>
<html lang="de">
<head>
<meta charset="utf-8">
<title>Personalvermittlung – Brauwalter GmbH</title>
<link rel="stylesheet" href="https://fonts.googleapis.com/css2?family=Arimo:wght@400;700&display=swap">
<style>
  :root {
    --teal: #179ca6;
    --teal-light: #b4dfe0;
    --dark: #383836;
    --panel-grey: #e6e6e6;
    --paper: #ffffff;
    --stage: #8a8a8a;
    --ink: #333333;
  }
  * { margin: 0; padding: 0; box-sizing: border-box; }
  html, body {
    width: 1200px; height: 1200px; overflow: hidden;
    background: var(--stage);
    font-family: "Arimo", Arial, sans-serif;
  }
  .flyer {
    position: absolute; left: 219px; top: 65px;
    width: 762px; height: 1069px;
    background: var(--paper); overflow: hidden;
  }
  .abs { position: absolute; }
  .hero-shapes { left: 0; top: 0; }
  .left-column-bg { left: 0; top: 205px; width: 381px; height: 676px; background: var(--panel-grey); }
  .photo-frame { left: 381px; top: 0; width: 381px; height: 345px; background: var(--teal-light); }
  .photo-area {
    left: 404px; top: 26px; width: 336px; height: 296px;
    background: linear-gradient(160deg, #4a63c8 0%, #9aa6c9 30%, #c9ccd0 50%, #8b8a7a 72%, #5d6a3c 100%);
  }
  .page-title {
    left: 23px; top: 25px; color: #fff; font-weight: 700;
    font-size: 34.5px; white-space: nowrap;
  }
  .bar { height: 8px; width: 32px; }
  .bar--light { background: #fff; }
  .bar--dark { background: var(--dark); }
  .intro {
    left: 23px; top: 115px; color: #fff;
    font-size: 14.9px; line-height: 20px; white-space: nowrap;
  }
  .section-title {
    font-weight: 700; font-size: 22px; color: var(--ink); white-space: nowrap;
  }
  .body-copy {
    font-size: 14.9px; line-height: 19.9px; color: var(--ink); white-space: nowrap;
  }
  .services .body-copy p + p { margin-top: 11px; }
  .benefits-section .body-copy p + p { margin-top: 6px; }
  .benefits { list-style: none; margin: 6px 0; }
  .benefits li { position: relative; padding-left: 24px; }
  .benefits li + li { margin-top: 5px; }
  .benefits li::before {
    content: ""; position: absolute; left: 2px; top: 4px;
    width: 11px; height: 11px; background: var(--teal);
  }
  .cta-band { left: 0; top: 881px; width: 762px; height: 82px; background: var(--dark); }
  .cta-icon { left: 62px; top: 8px; }
  .cta-heading {
    left: 144px; top: 27px; color: #fff; font-weight: 700; font-size: 25px; white-space: nowrap;
  }
  .cta-pill {
    left: 432px; top: 14px; width: 268px; height: 53px; border-radius: 27px;
    background: var(--teal); color: #fff; font-size: 14.9px; line-height: 20px;
    padding: 7px 0 0 27px; white-space: nowrap;
  }
  .contact-list { left: 23px; top: 964px; list-style: none; color: var(--ink); }
  .contact-list li { display: flex; align-items: center; gap: 9px; white-space: nowrap; }
  .contact-list .phone { font-weight: 700; font-size: 21px; height: 32px; }
  .contact-list .mail, .contact-list .web { font-size: 15px; height: 27px; }
  .footer-divider {
    left: 296px; top: 968px; width: 3px; height: 96px;
    background: linear-gradient(to bottom, rgba(0,0,0,0), rgba(0,0,0,0.35), rgba(0,0,0,0));
  }
  .company-name { left: 376px; top: 990px; color: var(--dark); white-space: nowrap; }
  .company-name .line-1 { font-weight: 700; font-size: 27px; letter-spacing: 0.5px; display: block; }
  .company-name .line-2 { font-weight: 700; font-size: 16.5px; display: block; margin-top: 1px; }
  .company-square { left: 673px; top: 980px; width: 65px; height: 65px; background: var(--teal); }
</style>
</head>
<body>
  <article class="flyer">
    <div class="abs left-column-bg"></div>
    <svg class="abs hero-shapes" width="381" height="345" viewBox="0 0 381 345" aria-hidden="true">
      <polygon points="0,0 381,0 381,205 0,345" fill="var(--teal)"/>
      <polygon points="232,260 381,205 381,345" fill="var(--dark)"/>
    </svg>

    <h1 class="abs page-title">Personalvermittlung</h1>
    <div class="abs bar bar--light" style="left:23px; top:75px;"></div>
    <p class="abs intro">
      Passende Mitarbeiter zu finden, stellt heute eine<br>
      große Herausforderung dar. Profitieren Sie von<br>
      unserem Netzwerk und unseren Kompetenzen im<br>
      Recruiting und entlasten Sie sich und Ihre<br>
      Abteilungsleiter, indem Sie uns mit der<br>
      Personalvermittlung beauftragen.
    </p>

    <div class="abs photo-frame"></div>
    <div class="abs photo-area" role="img" aria-label="Foto: Bürogebäude mit Firmenstele von Brauwalter, davor Kiesbeet mit Buchsbäumen"></div>

    <section class="abs services" style="left:23px; top:354px;">
      <h2 class="section-title">Unsere Dienstleistung</h2>
      <div class="bar bar--dark" style="margin:10px 0 11px 2px;"></div>
      <div class="body-copy">
        <p>Wir übernehmen die Suche nach Mitarbeitenden für<br>
        eine vakante Stelle in Ihrem Unternehmen. Der<br>
        Prozess wird ganz flexibel nach Ihren Wünschen<br>
        gestaltet – in der Regel erstellen Sie mit einem<br>
        unserer erfahrenen Recruiter das Anforderungsprofil,<br>
        anhand diesem gestalten wir die Stellenanzeige. Die<br>
        Veröffentlichung und die Selektion der<br>
        entsprechenden Kanäle bestimmen Sie<br>
        selbstverständlich mit.</p>
        <p>Die in der Folge eingehenden Bewerbungen<br>
        selektieren wir für jede Qualifikation und<br>
        Hierarchiestufe und führen erste Gespräche.<br>
        Anschließend präsentieren wir Ihnen die<br>
        ausgewählten Kandidaten. Alternativ stellen wir<br>
        Ihnen auch gerne alle eingegangenen Bewerbungen<br>
        vor – das machen wir ganz von Ihren Wünschen und<br>
        Vorstellungen abhängig.</p>
        <p>Auch beim Onboarding sind wir gerne<br>
        unterstützend da – hier gilt einmal mehr, alles kann,<br>
        nichts muss. Lassen Sie uns gerne die<br>
        verschiedenen Optionen besprechen.</p>
      </div>
    </section>

    <section class="abs benefits-section" style="left:396px; top:354px;">
      <h2 class="section-title">Vorteile der Personalvermittlung</h2>
      <div class="bar bar--dark" style="margin:10px 0 11px 0;"></div>
      <div class="body-copy">
        <p>Gerade für kleine und mittlere Betriebe, die nicht<br>
        über eine eigene Personalabteilung verfügen,<br>
        stellen Neueinstellungen und das damit<br>
        verbundene Recruiting oft eine große zeitliche<br>
        Herausforderung dar.</p>
        <p>Hier kann die Zusammenarbeit mit uns eine große<br>
        Entlastung sein:</p>
        <ul class="benefits">
          <li>Ihr Aufwand wird punktgenau nach außen<br>
          verlagert und Ihre Mitarbeiter können sich auf<br>
          Ihr Kerngeschäft konzentrieren</li>
          <li>Die Zusammenarbeit mit unseren erfahrenen<br>
          Recruitern bringt Mehrwert – vom Erstellen des<br>
          Anforderungsprofils über die Gestaltung der<br>
          Stellenanzeige bis zum Auswahlprozess<br>
          profitieren Sie von unserer jahrelangen<br>
          Erfahrung</li>
          <li>Über unser großes Netzwerk gelingt es uns,<br>
          mehr Bewerbungen in kürzerer Zeit zu<br>
          generieren</li>
        </ul>
        <p>Insgesamt profitieren Sie von unserer<br>
        Dienstleistung immer genau dann, wenn ein<br>
        Personalbedarf entsteht.</p>
      </div>
    </section>

    <div class="abs cta-band">
      <svg class="abs cta-icon" width="68" height="66" viewBox="0 0 68 66" aria-hidden="true">
        <path d="M24 22 h38 a5 5 0 0 1 5 5 v24 a5 5 0 0 1 -5 5 h-4 v9 l-10 -9 h-24 a5 5 0 0 1 -5 -5 v-24 a5 5 0 0 1 5 -5z" fill="var(--teal-light)"/>
        <path d="M5 0 h40 a5 5 0 0 1 5 5 v26 a5 5 0 0 1 -5 5 h-26 l-10 10 v-10 h-4 a5 5 0 0 1 -5 -5 v-26 a5 5 0 0 1 5 -5z" fill="var(--teal)" stroke="var(--dark)" stroke-width="2"/>
        <text x="25" y="27" text-anchor="middle" fill="#fff" font-family="Arimo, Arial, sans-serif" font-weight="700" font-size="24">?</text>
      </svg>
      <p class="abs cta-heading">Wir freuen uns auf Sie!</p>
      <p class="abs cta-pill">Sie haben weitere Fragen?<br>Dann kontaktieren Sie uns gerne.</p>
    </div>

    <ul class="abs contact-list">
      <li class="phone">
        <svg width="16" height="16" viewBox="0 0 24 24" aria-hidden="true"><path d="M6.6 10.8a15.2 15.2 0 0 0 6.6 6.6l2.2-2.2a1 1 0 0 1 1-.25 11.4 11.4 0 0 0 3.6.57 1 1 0 0 1 1 1V20a1 1 0 0 1-1 1A17 17 0 0 1 3 4a1 1 0 0 1 1-1h3.5a1 1 0 0 1 1 1c0 1.250.2 2.450.57 3.57a1 1 0 0 1-.25 1z" fill="var(--teal)"/></svg>
        +49 6881 47310
      </li>
      <li class="mail">
        <svg width="15" height="15" viewBox="0 0 24 24" aria-hidden="true"><path d="M2 11 L22 3 L17 21 L11 15 L18 7 L8 13z" fill="var(--teal)"/></svg>
        info@brauwalter.org
      </li>
      <li class="web">
        <svg width="15" height="15" viewBox="0 0 24 24" aria-hidden="true"><g fill="none" stroke="var(--teal)" stroke-width="2"><circle cx="12" cy="12" r="10"/><ellipse cx="12" cy="12" rx="4.5" ry="10"/><path d="M2 12h20M4 7h16M4 17h16"/></g></svg>
        www.brauwalter.org
      </li>
    </ul>

    <div class="abs footer-divider"></div>
    <p class="abs company-name">
      <span class="line-1">BRAUWALTER</span>
      <span class="line-2">Personaldienstleistungen GmbH</span>
    </p>
    <div class="abs company-square"></div>
  </article>
</body>
</html>
```